Visitenkarten-Design für Abbruch und Schadstoffsanierungsfirma
Zielgruppe
Wir sind ein Abbruch und Schadstoffsanierungsfirma aus Kassel und suchen einen eleganten unverwechselbaren Design für unsere Visitenkarten.
Zielgruppe: Alle
Aufgabenstellung
Gut lesbar alles

```html
<!DOCTYPE html>
<html lang="de">
<head>
<meta charset="utf-8">
<title>Harvelt – Visitenkarte</title>
<link rel="stylesheet" href="https://fonts.googleapis.com/css2?family=Ubuntu:wght@400;500&family=Rubik:ital,wght@0,400;0,600;1,400&display=swap">
<style>
  :root {
    --canvas: #343b3e;
    --shadow: #272d30;
    --paper: #ffffff;
    --navy: #0e1120;
    --brick: #a8261e;
    --stone: #d9d8de;
    --blush: #f1e0d9;
  }
  * { box-sizing: border-box; margin: 0; padding: 0; }
  html, body { width: 1200px; height: 1200px; overflow: hidden; }
  body { background: var(--canvas); position: relative; font-family: "Ubuntu", sans-serif; }

  .card {
    position: absolute; left: 170px; width: 860px; height: 495px;
    background: var(--paper); overflow: hidden;
    box-shadow: 20px 20px 0 var(--shadow);
  }
  .card--front { top: 70px; }
  .card--back { top: 635px; }

  .card__accent {
    position: absolute; top: 0; right: 0; width: 200px; height: 100%;
    background: linear-gradient(180deg, var(--blush) 0%, var(--stone) 100%);
  }

  .brand {
    position: absolute; display: flex; align-items: center; gap: 18px;
    color: var(--navy); font-family: "Ubuntu", sans-serif; font-weight: 500;
  }
  .brand__mark { background: var(--brick); flex: none; }
  .card--front .brand { left: 0; width: 660px; top: 175px; justify-content: center; font-size: 86px; letter-spacing: 2px; }
  .card--front .brand__mark { width: 50px; height: 50px; }
  .card--back .brand { left: 84px; top: 88px; font-size: 58px; letter-spacing: 1px; gap: 14px; }
  .card--back .brand__mark { width: 36px; height: 36px; }

  .services {
    position: absolute; left: 0; width: 660px; top: 406px;
    text-align: center; color: var(--brick); font-size: 20px; letter-spacing: 0.2px;
  }
  .services__dot { display: inline-block; width: 5px; height: 5px; background: var(--brick); margin: 0 11px; vertical-align: middle; }

  .person { position: absolute; left: 84px; top: 372px; }
  .person__name { font-family: "Rubik", sans-serif; font-weight: 600; font-size: 37px; color: var(--navy); line-height: 1.1; }
  .person__role { font-family: "Rubik", sans-serif; font-style: italic; font-size: 20px; color: var(--brick); margin-top: 4px; }

  .contact { position: absolute; left: 464px; top: 292px; list-style: none; font-family: "Rubik", sans-serif; font-size: 24px; color: var(--navy); }
  .contact__item { display: flex; align-items: flex-start; gap: 16px; line-height: 30px; margin-bottom: 6px; }
  .contact__icon { width: 24px; height: 24px; flex: none; margin-top: 3px; }
</style>
</head>
<body>
  <section class="card card--front" aria-label="Vorderseite">
    <div class="card__accent" role="img" aria-label="Dekorative Farbfläche in Hellgrau und Rosé"></div>
    <div class="brand"><span class="brand__mark"></span><span class="brand__name">Harvelt</span></div>
    <p class="services">Schadstoffsanierung<span class="services__dot"></span>Abbruch<span class="services__dot"></span>Entkernen</p>
  </section>

  <section class="card card--back" aria-label="Rückseite">
    <div class="brand"><span class="brand__mark"></span><span class="brand__name">Harvelt</span></div>
    <div class="person">
      <p class="person__name">Jorin Velkamp</p>
      <p class="person__role">Geschäftsführer</p>
    </div>
    <ul class="contact">
      <li class="contact__item">
        <svg class="contact__icon" viewBox="0 0 24 24" aria-hidden="true"><circle cx="12" cy="12" r="12" fill="var(--navy)"/><path d="M12 5a4.5 4.5 0 0 0-4.5 4.5c0 3.2 4.5 8.5 4.5 8.5s4.5-5.3 4.5-8.5A4.5 4.5 0 0 0 12 5z" fill="#fff"/><circle cx="12" cy="9.5" r="1.7" fill="var(--navy)"/></svg>
        <span>Lindenhofweg 14,<br>34117 Kassel</span>
      </li>
      <li class="contact__item">
        <svg class="contact__icon" viewBox="0 0 24 24" aria-hidden="true"><circle cx="12" cy="12" r="12" fill="var(--navy)"/><path d="M8.2 6.5l2 .2 1 2.6-1.3 1.1a7 7 0 0 0 3.7 3.7l1.1-1.3 2.6 1 .2 2c-.4.9-1.3 1.4-2.3 1.3A10 10 0 0 1 6.9 8.8c-.1-1 .4-1.9 1.3-2.3z" fill="#fff"/></svg>
        <span>01570 2284913</span>
      </li>
      <li class="contact__item">
        <svg class="contact__icon" viewBox="0 0 24 24" aria-hidden="true"><circle cx="12" cy="12" r="12" fill="var(--navy)"/><rect x="6" y="8" width="12" height="8.5" rx="1" fill="#fff"/><path d="M6.5 8.6l5.5 4.2 5.5-4.2" fill="none" stroke="var(--navy)" stroke-width="1.3"/></svg>
        <span>kontakt@harvelt-kassel.de</span>
      </li>
      <li class="contact__item">
        <svg class="contact__icon" viewBox="0 0 24 24" aria-hidden="true"><circle cx="12" cy="12" r="12" fill="var(--navy)"/><g fill="none" stroke="#fff" stroke-width="1.3"><circle cx="12" cy="12" r="6"/><ellipse cx="12" cy="12" rx="2.6" ry="6"/><path d="M6 12h12M7 9h10M7 15h10"/></g></svg>
        <span>harvelt-kassel.de</span>
      </li>
    </ul>
  </section>
</body>
</html>
```